4747 5858

Web(re)design of an existing directory search site www.le5858.be (in Dutch www.de4747.be and in English www.3737.be).

This site is a directory site, i.e. a "white pages" site whereby people can search the phone & details of another person based on a combination of name + city (for instance pellow in Brussels); one can also search a company also based on a combination of name + city (for instance Vornak in Brussels); last but not least one can also search the name of the subscriber behind a specific telephone number (also called reverse search).

This site is quite outdated and needs a redesign, see instructions.

We need the output in XD format.

```html
<!DOCTYPE html>
<html lang="en">
<head>
<meta charset="utf-8">
<title>58-58 – The ONE number for ALL directory enquiries</title>
<link rel="stylesheet" href="https://fonts.googleapis.com/css2?family=Montserrat:wght@300;400;500;600;700&family=Boogaloo&display=swap">
<style>
  :root {
    --ink: #5a4ea6;
    --ink-soft: #8a8aa0;
    --page: #f1f3fc;
    --white: #ffffff;
    --violet: #7b12f6;
    --violet-deep: #6a10ea;
    --violet-dark: #3b0a86;
    --pill: #dfe4fa;
    --line: #d6d8e8;
  }
  * { box-sizing: border-box; margin: 0; padding: 0; }
  html, body { width: 1200px; height: 1181px; overflow: hidden; }
  body {
    position: relative;
    background: var(--page);
    font-family: "Montserrat", sans-serif;
    color: var(--ink);
  }
  .abs { position: absolute; }
  .center { left: 0; width: 1200px; text-align: center; }

  /* header */
  .site-header { top: 0; left: 0; width: 1200px; height: 40px; background: var(--page); box-shadow: 0 1px 3px rgba(60,60,120,.15); }
  .brand { left: 279px; top: 4px; font-size: 25px; font-weight: 700; color: var(--ink); letter-spacing: -0.5px; }
  .tagline { left: 361px; top: 14px; font-size: 9.5px; font-weight: 500; }
  .nav-call { left: 709px; top: 9px; width: 63px; height: 20px; border-radius: 5px; background: var(--pill); font-size: 9.5px; line-height: 20px; text-align: center; }
  .nav-home { left: 801px; top: 14px; font-size: 9.5px; }
  .nav-lang { left: 857px; top: 14px; font-size: 9.5px; }
  .nav-lang svg { margin-left: 8px; vertical-align: middle; }

  /* hero */
  .hero-title { top: 88px; font-family: "Boogaloo", sans-serif; font-size: 31px; line-height: 27px; color: var(--ink); }
  .hero-sub { top: 161px; font-size: 17px; font-weight: 300; color: var(--ink-soft); }
  .search-title { top: 236px; font-size: 23px; font-weight: 400; }

  .tab { top: 281px; width: 147px; height: 38px; border: 1px solid var(--line); border-radius: 4px; background: var(--page); font-size: 8.5px; font-weight: 500; letter-spacing: .3px; line-height: 36px; text-align: center; }
  .tab.is-active { background: var(--violet); border-color: var(--violet); color: var(--white); }

  .field-label { top: 339px; font-size: 10.5px; font-weight: 500; }
  .field { top: 359px; width: 174px; height: 39px; border: 1px solid var(--line); border-radius: 6px; background: var(--white); }
  .btn-find { left: 840px; top: 359px; width: 93px; height: 38px; border-radius: 5px; background: linear-gradient(90deg, var(--violet), var(--violet-deep)); color: var(--white); font-size: 13.5px; font-weight: 700; line-height: 38px; text-align: center; }

  /* features band */
  .features { top: 485px; left: 0; width: 1200px; height: 210px; background: linear-gradient(90deg, #8612fa, var(--violet-deep)); }
  .features-title { left: 424px; top: 41px; font-size: 22px; font-weight: 700; color: var(--white); }
  .feature-list { top: 104px; width: 200px; list-style: none; text-align: center; color: var(--white); font-size: 12px; line-height: 16px; font-weight: 400; }
  .illustration { left: 780px; top: 22px; width: 153px; height: 188px; background: linear-gradient(170deg, #9e7af0 0%, #8a7ae6 60%, #8e84e0 100%); border-radius: 76px 76px 0 0; opacity: .9; }

  /* call band */
  .call-band { top: 695px; left: 0; width: 1200px; height: 111px; background: var(--white); box-shadow: 0 1px 3px rgba(60,60,120,.12); }
  .call-title { top: 18px; font-size: 18px; font-weight: 600; }
  .btn-call { left: 553px; top: 49px; width: 94px; height: 38px; border-radius: 4px; background: var(--violet); color: var(--white); font-size: 13.5px; font-weight: 600; line-height: 38px; text-align: center; }

  /* useful numbers */
  .numbers-title { top: 866px; font-size: 22px; font-weight: 600; }
  .number-card { top: 928px; width: 140px; text-align: center; }
  .number-card h3 { font-size: 22px; font-weight: 700; letter-spacing: -0.5px; }
  .number-card p { margin-top: 13px; font-size: 9px; font-weight: 300; line-height: 9.5px; color: var(--ink-soft); }

  /* footer */
  .footer { top: 1082px; left: 0; width: 1200px; height: 77px; background: linear-gradient(90deg, #8612fa, var(--violet-deep)); }
  .footer p { position: absolute; left: 375px; top: 24px; width: 450px; text-align: center; font-size: 7px; line-height: 6.7px; color: var(--white); }
  .copyright { top: 1159px; left: 0; width: 1200px; height: 22px; background: var(--violet-dark); color: var(--white); font-size: 8.5px; font-weight: 500; line-height: 22px; text-align: center; }
</style>
</head>
<body>

<header class="abs site-header">
  <div class="abs brand">58-58</div>
  <div class="abs tagline">The ONE number for ALL directory enquiries</div>
  <div class="abs nav-call">Call now!</div>
  <div class="abs nav-home">Home</div>
  <div class="abs nav-lang">English<svg width="8" height="5" viewBox="0 0 8 5"><path d="M1 1l3 3 3-3" fill="none" stroke="#5a4ea6" stroke-width="1.2"/></svg></div>
</header>

<h1 class="abs center hero-title">The ONE number<br>for ALL directory enquiries</h1>
<p class="abs center hero-sub">Looking for everyone and all</p>

<h2 class="abs center search-title">Who You Search?</h2>
<div class="abs tab is-active" style="left:267px">PEOPLE SEARCH</div>
<div class="abs tab" style="left:440px">COMPANIES</div>
<div class="abs tab" style="left:613px">REVERSE PHONE</div>
<div class="abs tab" style="left:786px">INTERNATIONAL</div>

<label class="abs field-label" style="left:277px">Firstname:</label>
<label class="abs field-label" style="left:468px">Lastname:</label>
<label class="abs field-label" style="left:657px">Locality:</label>
<div class="abs field" style="left:266px"></div>
<div class="abs field" style="left:457px"></div>
<div class="abs field" style="left:650px"></div>
<div class="abs btn-find">FIND</div>

<section class="abs features">
  <h2 class="abs features-title">What can I find on Listfinder?</h2>
  <ul class="abs feature-list" style="left:393px">
    <li>Cell phone numbers</li><li>Names</li><li>Lastnames</li><li>Addresses</li>
  </ul>
  <ul class="abs feature-list" style="left:616px">
    <li>Coompaies</li><li>International search</li><li>Professional licenses</li><li>Professional licenses</li>
  </ul>
  <div class="abs illustration" role="img" aria-label="Illustration of a hand holding a magnifying glass"></div>
</section>

<section class="abs call-band">
  <h2 class="abs center call-title">Want to find someone right now?</h2>
  <div class="abs btn-call">Call NOW!</div>
</section>

<h2 class="abs center numbers-title">Useful Numbers</h2>
<div class="abs number-card" style="left:362px"><h3>47-47</h3><p>There are many variations of passages of Lorem Ipsum available, but the majority have suffered alteration in some form, by injected humour</p></div>
<div class="abs number-card" style="left:530px"><h3>58-58</h3><p>There are many variations of passages of Lorem Ipsum available, but the majority have suffered alteration in some form, by injected humour</p></div>
<div class="abs number-card" style="left:689px"><h3>37-37</h3><p>There are many variations of passages of Lorem Ipsum available, but the majority have suffered alteration in some form, by injected humour</p></div>

<footer class="abs footer">
  <p>If you are going to use a passage of Lorem Ipsum, you need to be sure there isn't anything embarrassing hidden in the middle of text. All the Lorem Ipsum generators on the Internet tend to repeat predefined chunks as necessary, making this the first true generator on the Internet. It uses a dictionary of over 200 Latin words, combined with a handful of model sentence structures, to generate Lorem Ipsum which looks reasonable. The generated Lorem Ipsum is therefore always free from repetition, injected humour, or non-characteristic words etc.</p>
</footer>
<div class="abs copyright">©2017 Copyrighted by le5858.&nbsp; All rights reserved.</div>

</body>
</html>
```